New Business Card Design Project

Use the flyer uploaded and website www.brightoakbuilders.com for inspiration.
List Our Services on Backside of business cards
Martin Hollis
Harborline Renovations Inc.
Licensed General Contractors
858-471-9063

Contact Information for Business Card

Use the flyer uploaded and website www.brightoakbuilders.com for inspiration. List Our Services on Backside of business cards Martin Hollis Harborline Renovations Inc. Licensed General Contractors 858-471-9063

```html
<!DOCTYPE html>
<html lang="en">
<head>
<meta charset="utf-8">
<title>Harborline Renovations – Business Cards</title>
<link rel="stylesheet" href="https://fonts.googleapis.com/css2?family=Cinzel:wght@400;500&family=Cormorant+Garamond:wght@500;600&display=swap">
<style>
  :root {
    --page: #e9e6e1;
    --card: #101112;
    --card-edge: #1a1b1d;
    --line: #3a3b3e;
    --ink: #f2f2f2;
    --accent: #2a9be0;
    --decor-a: #1c1d20;
    --decor-b: #141517;
  }
  * { margin: 0; padding: 0; box-sizing: border-box; }
  html, body { width: 1200px; height: 900px; overflow: hidden; background: var(--page); }
  .canvas {
    position: relative; width: 1200px; height: 900px;
    display: flex; flex-direction: column; align-items: center; justify-content: center; gap: 48px;
  }
  .card {
    position: relative; width: 680px; height: 388px;
    background: var(--card); border-radius: 30px; overflow: hidden;
    box-shadow: 0 10px 28px rgba(0,0,0,.25);
    color: var(--ink);
    font-family: "Cormorant Garamond", Georgia, serif;
  }
  .decor {
    position: absolute; right: 0; top: 0; width: 330px; height: 250px;
    background: radial-gradient(ellipse at 60% 40%, var(--decor-a), var(--decor-b) 70%, transparent);
  }
  .divider { position: absolute; inset: 0; width: 100%; height: 100%; }
  .divider polyline { fill: none; stroke: var(--line); stroke-width: 2; }

  .services { position: absolute; left: 38px; top: 40px; width: 430px; }
  .services-title {
    font-family: "Cinzel", Georgia, serif; font-weight: 500;
    color: var(--accent); font-size: 22px; letter-spacing: 1px; margin-bottom: 6px;
  }
  .services-list { list-style: none; font-size: 17px; font-weight: 600; line-height: 1.3; }

  .brand {
    position: absolute; font-weight: 600; letter-spacing: 2px;
    text-transform: uppercase; color: var(--ink); display: flex; align-items: center; gap: 10px;
  }
  .brand-dot { width: 10px; height: 10px; border-radius: 50%; background: var(--ink); }
  .back .brand { left: 38px; bottom: 42px; font-size: 22px; }

  .guarantee {
    position: absolute; right: 54px; bottom: 100px; width: 280px;
    color: var(--accent); font-size: 34px; font-weight: 500; line-height: 1.05; text-align: center;
  }

  .front .brand { left: 40px; top: 120px; font-size: 24px; }
  .person { position: absolute; left: 40px; top: 208px; }
  .person-name {
    font-family: "Cinzel", Georgia, serif; font-weight: 500;
    color: var(--accent); font-size: 32px; letter-spacing: 1px; line-height: 1.1;
  }
  .person-role { font-size: 21px; font-weight: 600; line-height: 1.15; }

  .contact { position: absolute; right: 40px; top: 212px; width: 300px; text-align: right; }
  .contact-cta { color: var(--accent); font-size: 27px; font-weight: 600; margin-bottom: 6px; }
  .contact-line { display: flex; justify-content: flex-end; align-items: center; gap: 8px; font-size: 21px; font-weight: 600; line-height: 1.35; }
  .contact-line svg { width: 18px; height: 18px; stroke: var(--accent); fill: none; stroke-width: 1.8; }
</style>
</head>
<body>
<main class="canvas">

  <section class="card back" aria-label="Business card back">
    <div class="decor" role="img" aria-label="Faint brand decoration area"></div>
    <svg class="divider" viewBox="0 0 680 388" aria-hidden="true">
      <polyline points="330,388 300,200 560,150 680,150"/>
    </svg>
    <div class="services">
      <h2 class="services-title">Our Services</h2>
      <ul class="services-list">
        <li>Remodel - Kitchen &amp; Bath / Painting - Interior &amp; Exterior</li>
        <li>Flooring - Carpet, Vinyl, Wood / Window &amp; Door Replacement</li>
        <li>Plumbing - Repairs &amp; Upgrades / Energy - Efficient Upgrades</li>
        <li>Deck &amp; Patio Construction / Water &amp; Mold Damage</li>
        <li>Garage Renovation</li>
      </ul>
    </div>
    <div class="brand"><span class="brand-dot"></span>Harborline Renovations</div>
    <p class="guarantee">Our Services Are 100% Guaranteed</p>
  </section>

  <section class="card front" aria-label="Business card front">
    <div class="decor" role="img" aria-label="Faint brand decoration area"></div>
    <svg class="divider" viewBox="0 0 680 388" aria-hidden="true">
      <polyline points="350,388 320,200 580,150 680,150"/>
    </svg>
    <div class="brand"><span class="brand-dot"></span>Harborline Renovations</div>
    <div class="person">
      <h1 class="person-name">MARTIN HOLLIS</h1>
      <p class="person-role">Harborline Renovations Inc.</p>
      <p class="person-role">Licensed General Contractors</p>
    </div>
    <div class="contact">
      <p class="contact-cta">Call/Text Or Book Online</p>
      <p class="contact-line">858-471-9063
        <svg viewBox="0 0 24 24" aria-hidden="true"><path d="M5 3h4l2 5-2.5 1.5a11 11 0 0 0 6 6L16 13l5 2v4a2 2 0 0 1-2 2A16 16 0 0 1 3 5a2 2 0 0 1 2-2z"/></svg>
      </p>
      <p class="contact-line">www.brightoakbuilders.com
        <svg viewBox="0 0 24 24" aria-hidden="true"><circle cx="12" cy="12" r="9"/><path d="M3 12h18M12 3c3 3 3 15 0 18M12 3c-3 3-3 15 0 18"/></svg>
      </p>
    </div>
  </section>

</main>
</body>
</html>
```